Healthy lifestyle Influencer business card

I need your creativity to have a business card that I can leave in all the restaurants, hotels and spas I visit to inform them that I am an influencer specializing in the wellness sector and that I will write a review about them. You can use my instagram photos Velusport72 or on my website www.piattileggerinuovi.it. I would like my business card to impress with its creativity! thank you very much!

Contact Information for Business Card

siteweb, instagram, phone number

Font styles to use
Decorative
Script

Colors
0094D4
00A9DD
6FCCEA
C7EBF8
E9F6FB
59FF00
82FF00
B8FF75
E3FFCB
F4FFEA
FFC000
F8CF3A
FAE287
FDF2CF
FEFAEE
F0912C
F2A743
F7CA91
FBE8D2
FDF5EE
EE7325
F08F49
F5BC92
FAE3D3
FDF4ED
EB3D1F
EC4F4E
F09395
F8D3D4
FCEDEE
E54698
E96AAD
F1A4CE
F9D9EA
FCEFF6

Requirements
Nice to have
• creativity

```html
<!DOCTYPE html>
<html lang="it">
<head>
<meta charset="utf-8">
<title>Velia – Business Card</title>
<link rel="stylesheet" href="https://fonts.googleapis.com/css2?family=Mrs+Saint+Delafield&family=Poppins:wght@300;400;500;600&display=swap">
<style>
  :root {
    --page: #f2f2f2;
    --card: #fdf4ed;
    --coral: #ec4f4e;
    --red: #eb3d1f;
    --orange: #ee7325;
    --blush: #f8d3d4;
    --leaf-dark: #2f4a22;
    --leaf: #5b7a3a;
    --ink: #111111;
  }
  * { box-sizing: border-box; margin: 0; padding: 0; }
  html, body {
    width: 1030px;
    height: 1200px;
    overflow: hidden;
    background: var(--page);
  }
  .canvas {
    position: relative;
    width: 1030px;
    height: 1200px;
  }
  .card {
    position: absolute;
    left: 26px;
    top: 306px;
    width: 978px;
    height: 600px;
    background: var(--card);
    overflow: hidden;
    box-shadow: 0 14px 30px rgba(0,0,0,0.18);
  }
  .card-decor {
    position: absolute;
    inset: 0;
    width: 978px;
    height: 600px;
  }
  .name {
    position: absolute;
    left: 52px;
    top: 150px;
    font-family: "Mrs Saint Delafield", cursive;
    font-size: 210px;
    line-height: 1;
    color: var(--coral);
    font-weight: 400;
  }
  .role {
    position: absolute;
    left: 160px;
    top: 345px;
    font-family: "Poppins", sans-serif;
    font-weight: 500;
    font-size: 33px;
    color: var(--ink);
    white-space: nowrap;
  }
  .divider {
    position: absolute;
    left: 80px;
    top: 452px;
    width: 350px;
    height: 1px;
    background: var(--coral);
  }
  .contact {
    position: absolute;
    left: 77px;
    top: 462px;
    font-family: "Poppins", sans-serif;
    color: var(--ink);
  }
  .contact-label {
    display: flex;
    align-items: center;
    gap: 5px;
    font-weight: 600;
    font-size: 23px;
    line-height: 1.3;
  }
  .contact-label::before {
    content: "";
    width: 10px;
    height: 19px;
    background: var(--coral);
  }
  .contact-value {
    padding-left: 16px;
    font-weight: 400;
    font-size: 27px;
    line-height: 1.3;
  }
</style>
</head>
<body>
<main class="canvas">
  <section class="card">
    <svg class="card-decor" viewBox="0 0 978 600" xmlns="http://www.w3.org/2000/svg">
      <!-- corner blush -->
      <path d="M0 505 C60 515 120 550 165 600 L0 600 Z" fill="var(--blush)"/>
      <!-- orange brush ring -->
      <path d="M565 0 L978 0 L978 300 C960 420 870 470 760 465 C650 460 560 410 520 330 C495 260 510 150 540 80 C550 50 560 20 565 0 Z" fill="var(--orange)"/>
      <!-- red accent -->
      <path d="M815 0 L978 0 L978 90 C940 110 880 115 840 90 C820 60 815 25 815 0 Z" fill="var(--red)" opacity="0.9"/>
      <!-- blush circle -->
      <circle cx="862" cy="465" r="110" fill="var(--blush)"/>
      <!-- portrait -->
      <defs>
        <radialGradient id="photoTone" cx="50%" cy="45%" r="60%">
          <stop offset="0%" stop-color="#8a7a52"/>
          <stop offset="55%" stop-color="var(--leaf)"/>
          <stop offset="100%" stop-color="var(--leaf-dark)"/>
        </radialGradient>
      </defs>
      <circle cx="752" cy="228" r="228" fill="url(#photoTone)" role="img" aria-label="Portrait photo of the influencer holding a fruit among green leaves"/>
    </svg>

    <h1 class="name">Velia</h1>
    <p class="role">Healthy Food Influencer</p>
    <div class="divider"></div>
    <div class="contact">
      <p class="contact-label">Website</p>
      <p class="contact-value">www.piattileggerinuovi.it</p>
    </div>
  </section>
</main>
</body>
</html>
```